Crest Porter Website Professional and Crisp Redesign

Hi Teams,
Good evening! I am looking for a Warm Crisp and Professional redesign of my company's website at www.CrestPorter.example. Please google "Valet Trash" also to see the low rent stuff my competition is doing. I have included so much material for you to help your creative minds collaborate with. We use Wordpress now and have a mobile app plug in that is using xmlrpc to communicate back and forth iOS and Android. Swift for iOS and Java for android. Wordpress for the site. Good Luck!
Heres a little test site we fooled around with http://crest.kmorr.example to get ideas flowing, if needed.
Use the new content and redesign file for page content/copy. We all add information like Bio's when we get there.
I want you to be creative - use your own words, just be crisp about it.
Home Page:
Concept:
Nice marsh/tide/palm tree image of a community, poised up to the sky.
Crest porter sign for each of the respective redirections/pages. (4 total)
Statement:
Crest Porter is a leading valet trash and recycling service provider offering robust and flexible solutions for your community’s recycling, waste and maintenance needs. Connect with us and let us give you and your residents the experience they deserve: Better people, better processes, and better technologies.
Video –
Client Login – top left always
Slogan – Improve the day with valet.
Tabs: (Could be in boxes or the Crest Porter sign)
1. Residents
2. Property Management
3. About us
4. Contact
Residents Page:
Dear Resident,
Making sure that our environment and communities stay beautiful is a part of Crest Porter’s mission. We owe it to ourselves to be more thoughtful in our own waste production by ensuring the items we discard have fulfilled their highest and best uses. We are thankful for the steps we take together that propel us in the right direction.
Video.
Why Valet:
Crest Porter solves the embarrassment and effort of handling waste and recycling for the sophisticated multifamily resident. We always like to say – find us one person who likes to take out the trash…
Service guidelines on display and downloadable.
Oops!
Picture of an example oops note –
Get one of these?! No sweat, just correct the checked box the next night and we will happily take your trash/recycling the next scheduled service evening.
Essentials:
1. Trash is tied, bagged, and in the provided container.
(max 2 bags, 25 lbs/night)
2. Ensure bins are placed and returned at the agreed upon times.
3. Always feel free to contact us with any questions, comments, or concerns.
Management Page
Dear Management,
As our multifamily industry grows and continues to evolve with our residents, add value industries like Valet Trash are emerging as best bets for better serving your community as a whole. Knowing the industry as we do, Crest Porter knows that how we perform in New York, directly impacts our teams opportunities in Florida. By instilling this united culture we are consistently able to outperform our industry’s key performance indicators such as retention rate that affords Crest Porter the advantage in most cases.
Video:
Why Crest?
1. Our Values –
Integrity | We are transparent and forthright in what we do.
Outstanding Customer Service | For us this means doing more than just what we are compensated for.
Accountability | In our industry, it’s the one miss that is remembered, so we always have redundancy plans and the technology needed to keep our clients well rested.
Strong Work Ethic | Discipline is the cornerstone of great results, and reliability.
2. Our People –
Crest Porter hosts tryouts, not interviews for all its thoroughly background checked employees. Tryouts ensure our high standards of integrity, accountability, and strong work ethics are consistently observed before allowing them on-site alone.
3. Our Process –
Our employee’s are trained to be safe problem solvers from the start. We take a 500-foot view above the job scope to develop safer, more efficient, and through ways of improving our work and culture. Then, we listen.
4. Our Technology –
Technology has allowed Crest Porter to better bridge the communication gap for our clients to get on-site performance data real time. Our application, H2H (Hall to hall), allows fast accurate reporting of our job assignments. This tool takes out the guesswork and follow up time when we have inquires.
5. Our Dividends –
No need to budget when our service generates profit infinitely with no start up investment through our phase in programs. We will always consider buying out the current provider’s contract as requested.
6. Our Involvements –
A chief aim for Crest Porter is to uplift and connect with our teammates, our clients, and our communities. We always find brilliant ways to contribute both with micro and macro impacts consistently. Check the attendance records of your local and national meetings and events – you’ll see that we show up. We are committed.
Connect with us to inquire more information and pricing
Info@CrestPorter.example | 885- CRST-PQL
Download information package
About
Hi There,
After spilling leaking trash in a brand new car on the way to the community compactor, enough was enough. The company was formed that same evening and the founder turned in his safe executive roll for a fortune 500 company and dove into the world of the unknown – Entrepreneurship. Through the merits of our service, self-investment, and teach-ability index Crest Porter is fast becoming a stable leader in setting the standard for valet trash.
Video
Leadership
Executive Team
Ray Fenwick
Glen Matusiak
Tara Hollins
Marla Quenvick
Ingrid Falkner
Area Management
New York
South Carolina
North Carolina
Georgia
Florida
Louisiana
Alabama
Texas
Contact page:
Pretty straight forward.
Again Good Luck!
Ray Fenwick
President
Crest Porter
Target Market(s)
Professionals
Industry/Entity Type
Apartment
Number of Pages Required
5+ page
Font styles to use
Requirements
Must have
- Professional, Organized, and Crisp
Nice to have
- You go out on your own and put your own touch on it. That would be refreshing.
Should not have
- Don't use the word "Complex" to talk about apartments. Have fun!

```html
<!DOCTYPE html>
<html lang="en">
<head>
<meta charset="utf-8">
<title>Crest Porter — Valet Waste Management Services</title>
<link href="https://fonts.googleapis.com/css2?family=Fira+Sans:wght@400;500;600&family=Yellowtail&display=swap" rel="stylesheet">
<style>
:root{
  --ink:#222;
  --body-text:#666;
  --white:#fff;
  --accent:#1ea1dd;
  --step-bg:#cfe6f2;
  --mint:#d3ebe6;
  --page-dark:#1c1e21;
  --page-darker:#121315;
  --footer-text:#c9c9c9;
  --signup:#7fcaec;
}
*{box-sizing:border-box;margin:0;padding:0}
html,body{width:1200px;height:2459px;overflow:hidden}
body{
  position:relative;
  font-family:"Fira Sans",Arial,sans-serif;
  color:var(--ink);
  background:linear-gradient(180deg,var(--page-dark) 0,var(--page-dark) 2221px,var(--page-darker) 2221px);
}
.hero{
  position:absolute;left:0;top:0;width:1200px;height:600px;
  background:
    linear-gradient(180deg,rgba(28,30,33,0) 78%,var(--page-dark) 100%),
    radial-gradient(ellipse 220px 160px at 600px 320px,#f7c04a 0,#e9862a 40%,rgba(200,90,30,0) 100%),
    linear-gradient(180deg,#c4561e 0,#e48a31 28%,#b85a24 46%,#3a2a22 56%,#4f4038 70%,#2b2a2a 100%);
}
.brand{position:absolute;left:111px;top:26px;display:flex;align-items:center;gap:12px}
.brand-mark{width:44px;height:44px;border-radius:50%;background:var(--white)}
.brand-name{font-size:30px;font-weight:600;color:var(--white)}
.top-actions{position:absolute;left:813px;top:31px;display:flex;gap:11px}
.btn-top{height:36px;display:flex;align-items:center;justify-content:center;font-size:12px;font-weight:500;text-transform:uppercase;border-radius:3px}
.btn-quote{width:146px;border:1px solid var(--white);color:var(--white)}
.btn-login{width:118px;background:var(--white);color:var(--ink)}
.main-nav{position:absolute;top:92px;right:112px;display:flex;gap:25px;font-size:12px;font-weight:500;color:var(--white);text-transform:uppercase}
.hero-title{position:absolute;left:108px;top:371px;font-size:32px;font-weight:500;color:var(--white)}
.btn-start{position:absolute;left:111px;top:429px;width:114px;height:36px;border:1px solid var(--white);border-radius:3px;color:var(--white);font-size:12px;font-weight:500;display:flex;align-items:center;justify-content:center;text-transform:uppercase}
.video-card{position:absolute;left:780px;top:333px;width:308px;height:177px;background:var(--white);padding:6px}
.video-frame{width:100%;height:100%;background:linear-gradient(90deg,#f2f2f2 0,#e8e8e8 55%,#aab5a0 70%,#c8cfc4 100%);position:relative}
.video-play{position:absolute;left:118px;top:66px}
.video-label{position:absolute;left:866px;top:515px;font-family:"Yellowtail",cursive;font-size:22px;color:var(--white)}

.tab{position:absolute;left:466px;top:594px}
.tab span{position:absolute;left:0;top:0;width:262px;height:46px;display:flex;align-items:center;justify-content:center;color:var(--white);font-size:21px;font-weight:500}

.content{position:absolute;left:111px;top:639px;width:977px;height:1643px;background:var(--white);border-radius:3px}
.steps{position:absolute;left:14px;top:17px;display:flex;gap:13px}
.step{width:308px;height:400px;background:var(--step-bg);text-align:center}
.step-photo{height:203px}
.step h3{font-size:19px;font-weight:500;margin-top:20px}
.step .time{font-size:13px;margin-top:6px;color:#333}
.step p{font-size:13px;line-height:20px;color:#333;margin:22px 26px 0}
.photo-a{background:linear-gradient(135deg,#8e949a,#d9d3c9 60%,#4a4e52)}
.photo-b{background:linear-gradient(135deg,#6e747a,#c9c3a6 50%,#5a5f58)}
.photo-c{background:linear-gradient(135deg,#8a8f94,#d5a24c 45%,#6f7377)}

.section-title{position:absolute;left:0;width:977px;text-align:center;font-size:21px;font-weight:500}
.section-title::after{content:"";display:block;width:66px;height:2px;background:var(--accent);margin:10px auto 0}
.section-text{position:absolute;text-align:center;font-size:16.5px;line-height:24px;color:var(--body-text)}
.statement-title{top:466px}
.statement-text{left:72px;width:833px;top:522px}

.who{position:absolute;left:14px;top:639px;width:950px;height:276px;display:flex}
.who-copy{width:475px;background:var(--mint);padding:20px 25px}
.who-copy h2{font-size:21px;font-weight:500}
.who-copy p{font-size:13px;line-height:19.5px;color:#333;margin-top:8px}
.btn-outline{display:inline-flex;align-items:center;justify-content:center;height:36px;border:1.5px solid var(--ink);border-radius:3px;font-size:12px;font-weight:500;text-transform:uppercase}
.who-copy .btn-outline{width:114px;margin-top:17px}
.who-photo{width:475px;background:linear-gradient(180deg,#7fb2de 0,#b9d5ec 35%,#d8dcdf 55%,#7fc6d6 80%,#c9c9c4 100%)}

.mission-title{top:963px}
.mission-text{left:188px;width:601px;top:1017px}

.features{position:absolute;left:14px;top:1133px;display:flex;gap:15px}
.feature{width:468px;text-align:center}
.feature:last-child{width:467px}
.feature-photo{height:274px}
.photo-exp{background:linear-gradient(160deg,#9fb0bf 0,#c9c2b6 45%,#7d8a6c 75%,#a7443f 100%)}
.photo-map{background:#e3e5e6;position:relative}
.feature h3{font-size:21px;font-weight:500;margin-top:22px}
.feature p{font-size:13px;line-height:20.5px;color:#333;margin:8px 28px 0}
.feature .btn-outline{width:114px;margin-top:14px}

.newsletter{position:absolute;left:111px;top:2325px}
.newsletter h4{font-size:16px;font-weight:600;color:var(--white)}
.newsletter p{font-size:12.5px;line-height:17px;color:var(--footer-text);margin-top:8px;width:330px}
.signup{position:absolute;left:454px;top:2354px;display:flex;gap:10px}
.signup .field{width:251px;height:36px;background:var(--white);border-radius:2px;font-size:12px;color:#999;padding:0 16px;display:flex;align-items:center}
.signup .submit{width:86px;height:36px;background:var(--signup);color:var(--white);font-size:12px;display:flex;align-items:center;justify-content:center;text-transform:uppercase}
.follow{position:absolute;left:946px;top:2325px}
.follow h4{font-size:16px;font-weight:600;color:var(--white)}
.follow .icons{display:flex;gap:7px;margin-top:11px}
.follow .icons span{width:35px;height:35px;background:#8a8a8a;display:block}
.footer-rule{position:absolute;left:0;top:2411px;width:1200px;height:1px;background:#2a2c2f}
.footer-nav{position:absolute;left:111px;top:2429px;font-size:12.5px;color:var(--footer-text)}
.footer-nav span{margin:0 8px;color:#777}
.copyright{position:absolute;right:112px;top:2429px;font-size:12.5px;color:var(--footer-text)}
</style>
</head>
<body>

<header class="hero" role="img" aria-label="Sunset over a marsh with tall pine silhouettes">
</header>
<div class="brand"><span class="brand-mark"></span><span class="brand-name">Crest Porter</span></div>
<div class="top-actions">
  <a class="btn-top btn-quote">Request a Quote</a>
  <a class="btn-top btn-login">Client Login</a>
</div>
<nav class="main-nav"><a>Residents</a><a>Property Management</a><a>About Us</a><a>Contact</a></nav>
<h1 class="hero-title">Improve the day with valet</h1>
<a class="btn-start">Get Started</a>
<div class="video-card">
  <div class="video-frame" role="img" aria-label="Video thumbnail: company presenter beside an aerial view of an apartment community">
    <svg class="video-play" width="34" height="24" viewBox="0 0 34 24"><rect width="34" height="24" rx="5" fill="#666"/><path d="M13 6l9 6-9 6z" fill="#fff"/></svg>
  </div>
</div>
<div class="video-label">Watch Our Video</div>

<div class="tab">
  <svg width="262" height="46" viewBox="0 0 262 46"><path d="M0 46C18 46 20 0 50 0H212C242 0 244 46 262 46Z" fill="#1ea1dd"/></svg>
  <span>How It Works</span>
</div>

<main class="content">
  <div class="steps">
    <article class="step">
      <div class="step-photo photo-a" role="img" aria-label="Valet bin placed by an apartment door"></div>
      <h3>Placement</h3>
      <div class="time">Sunday - Thursday 6 to 8pm.</div>
      <p>All trash should be securely tied and placed in Crest Porter bin. Double bag all pet waste. Up to 2 bags per night under 25 pounds</p>
    </article>
    <article class="step">
      <div class="step-photo photo-b" role="img" aria-label="Team member in safety vest collecting trash"></div>
      <h3>Pickup</h3>
      <div class="time">Sunday - Thursday 8 to 11pm.</div>
      <p>Background screened and proven Crest team member performs valet service.</p>
    </article>
    <article class="step">
      <div class="step-photo photo-c" role="img" aria-label="Resident bringing the emptied bin inside"></div>
      <h3>Return</h3>
      <div class="time">Sunday - Thursday 9am Next Day</div>
      <p>Place the emptied Crest Porter bin back inside the residence the following morning.</p>
    </article>
  </div>

  <h2 class="section-title statement-title">Our Statement</h2>
  <p class="section-text statement-text">Crest Porter is a leading valet trash and recycling service provider offering robust and flexible solutions for your community’s recycling, waste and maintenance needs. Connect with us and let us give you and your residents the experience they deserve: Better people, better processes, and better technologies.</p>

  <section class="who">
    <div class="who-copy">
      <h2>Who We Are</h2>
      <p>Class aptent taciti sociosqu ad litora torquent per conubia nostra, per inceptos himenaeos. Mauris in erat justo. Nullam ac urna eu felis dapibus condimentum sit amet a augue. Sed non neque elit. Sed ut imperdiet nisi. Proin condimentum fermentum nunc. Etiam pharetra, erat sed fermentum feugiat, velit mauris egestas quam, ut aliquam massa nisl quis neque. Suspendisse in orci enim. This is vitae erat consequat auctor eu in elit.</p>
      <a class="btn-outline">Learn More</a>
    </div>
    <div class="who-photo" role="img" aria-label="Apartment community with pool under a blue sky"></div>
  </section>

  <h2 class="section-title mission-title">Our Mission</h2>
  <p class="section-text mission-text">Just like the tides renew and recycle the oceans, Crest porter rejuvenates communities by offering streamlined waste removal and recycling. What an opportunity to water the seed of renewal.</p>

  <div class="features">
    <article class="feature">
      <div class="feature-photo photo-exp" role="img" aria-label="Smiling team member in safety vest outside apartments"></div>
      <h3>Experience</h3>
      <p>Class aptent taciti sociosqu ad litora torquent per conubia nostra, per inceptos himenaeos. Mauris in erat justo. Nullam ac urna eu felis dapibus condimentum sit amet a augue. Sed non neque elit. Sed ut imperdiet nisi. Proin condimentum fermentum nunc.</p>
      <a class="btn-outline">Learn More</a>
    </article>
    <article class="feature">
      <div class="feature-photo photo-map" role="img" aria-label="Map of the United States highlighting southeastern service states"></div>
      <h3>Locations</h3>
      <p>Class aptent taciti sociosqu ad litora torquent per conubia nostra, per inceptos himenaeos. Mauris in erat justo. Nullam ac urna eu felis dapibus condimentum sit amet a augue. Sed non neque elit. Sed ut imperdiet nisi. Proin condimentum fermentum nunc.</p>
      <a class="btn-outline">Learn More</a>
    </article>
  </div>
</main>

<footer>
  <div class="newsletter">
    <h4>Sign Up Newsletter!</h4>
    <p>Sign up today for our newsletter and receive latest news and also get our tips &amp; exclusive offers.</p>
  </div>
  <div class="signup"><span class="field">Email Address</span><span class="submit">Sign Up</span></div>
  <div class="follow">
    <h4>Follow Us</h4>
    <div class="icons"><span></span><span></span></div>
  </div>
  <div class="footer-rule"></div>
  <div class="footer-nav">Home<span>|</span>Residents<span>|</span>Property Management<span>|</span>About Us<span>|</span>Contact</div>
  <div class="copyright">© 2017 Crest Porter</div>
</footer>

</body>
</html>
```